Personal Trainer and Corporate Health Business

I need a business card for a new company I'm starting in Australia called "Brisk Vigour Outreach" I will be providing a Personal training service as well as corporate health in companies.
The service provided is to help promote an active and healthy lifstyle.
The design should communicate a healthy lifestyle and also the benefits that this can have on a personal level and in the corporate environment and the benefits that flow from that.

Target Market(s)

Members of the public and Corporate

Industry/Entity Type

Environment

Requirements
Must have
• Company logo attached
Look and feel fresh and modern

Tag line: "Moving you toward a fitter, fuller life"

Colin Varga
Managing Director

m: 0412 657 394
e: colin@briskvigouroutreach.com.au

www.briskvigouroutreach.com.au
Nice to have
• Can be 1 or 2 sided

```html
<!DOCTYPE html>
<html lang="en">
<head>
<meta charset="utf-8">
<title>Brisk Vigour Outreach – Business Card</title>
<link rel="stylesheet" href="https://fonts.googleapis.com/css2?family=Open+Sans:ital,wght@0,400;0,600;0,700;1,400&display=swap">
<style>
  :root {
    --brand-blue: #0b5cad;
    --brand-green: #8dc63f;
    --text-grey: #7a7a7a;
    --card-white: #ffffff;
    --page-bg: #e4e6ea;
  }
  * { box-sizing: border-box; margin: 0; padding: 0; }
  html, body {
    width: 1200px; height: 900px; overflow: hidden;
    background: var(--page-bg);
    font-family: "Open Sans", Arial, sans-serif;
  }
  .stage {
    width: 1200px; height: 900px;
    display: flex; flex-direction: column; align-items: center; justify-content: center;
    gap: 40px;
  }
  .card {
    position: relative;
    width: 700px; height: 400px;
    background: var(--card-white);
    box-shadow: 0 6px 18px rgba(0,0,0,0.18);
    overflow: hidden;
  }
  .card::before, .card::after {
    content: ""; position: absolute; left: 0; right: 0;
    background: var(--brand-blue);
  }
  .card::before { top: 0; height: 22px; }
  .card::after { bottom: 0; height: 26px; }

  /* Front */
  .card-front { display: flex; align-items: center; }
  .wordmark {
    color: var(--brand-blue);
    font-weight: 600;
    text-transform: uppercase;
    letter-spacing: 0.04em;
    line-height: 1.15;
  }
  .card-front .wordmark {
    width: 300px; padding-left: 50px;
    font-size: 24px;
  }
  .divider {
    width: 2px; height: 180px;
    background: var(--brand-blue);
  }
  .contact { padding-left: 24px; }
  .person-name {
    color: var(--brand-blue);
    font-size: 22px; font-weight: 700;
    text-transform: uppercase; letter-spacing: 0.02em;
    line-height: 1.1;
  }
  .person-role {
    color: var(--text-grey);
    font-size: 12px; font-weight: 600;
    text-transform: uppercase; letter-spacing: 0.04em;
    margin-bottom: 18px;
  }
  .contact-list { list-style: none; }
  .contact-list li {
    display: flex; align-items: center; gap: 12px;
    color: var(--text-grey);
    font-size: 14px; line-height: 1.5;
  }
  .contact-list svg { width: 12px; height: 12px; flex: none; }

  /* Back */
  .card-back {
    display: flex; flex-direction: column; align-items: center; justify-content: center;
  }
  .card-back .wordmark { font-size: 40px; text-align: center; }
  .tagline {
    margin-top: 22px;
    color: var(--brand-green);
    font-size: 15px; font-style: italic;
  }
</style>
</head>
<body>
<main class="stage">
  <section class="card card-front">
    <div class="wordmark">Brisk Vigour<br>Outreach</div>
    <div class="divider"></div>
    <div class="contact">
      <p class="person-name">Colin Varga</p>
      <p class="person-role">Managing Director</p>
      <ul class="contact-list">
        <li>
          <svg viewBox="0 0 12 12" aria-hidden="true"><rect x="3" y="0.5" width="6" height="11" rx="1.2" fill="var(--brand-blue)"/><rect x="4.2" y="2" width="3.6" height="5" fill="#fff"/></svg>
          0412 657 394
        </li>
        <li>
          <svg viewBox="0 0 12 12" aria-hidden="true"><rect x="0.5" y="2.5" width="11" height="7" fill="var(--brand-blue)"/><path d="M0.8 2.8 L6 6.8 L11.2 2.8" stroke="#fff" stroke-width="1" fill="none"/></svg>
          colin@briskvigouroutreach.com.au
        </li>
        <li>
          <svg viewBox="0 0 12 12" aria-hidden="true"><circle cx="6" cy="6" r="5.2" fill="none" stroke="var(--brand-blue)" stroke-width="1.2"/><ellipse cx="6" cy="6" rx="2.2" ry="5.2" fill="none" stroke="var(--brand-blue)" stroke-width="1"/><line x1="0.8" y1="6" x2="11.2" y2="6" stroke="var(--brand-blue)" stroke-width="1"/></svg>
          www.briskvigouroutreach.com.au
        </li>
      </ul>
    </div>
  </section>

  <section class="card card-back">
    <div class="wordmark">Brisk Vigour Outreach</div>
    <p class="tagline">“Moving you toward a fitter, fuller life”</p>
  </section>
</main>
</body>
</html>
```